Business card, postcard, pocket folder

We are a real estate team and have had a new logo designed. From this, we need the following deliverables:- Business Cards (double-sided)- Just Listed / Just Sold Postcards (double-sided)- Pocket Folder. See logo attached.More work possible for the winning designer.
There are 5 members of the team, so head shots should be easily changed and possible for a group photo might be a good idea for the pocket folder but not 100% neccessary.
Target Market(s)
Real estate
Industry/Entity Type
Real Estate
Font styles to use
Serif
Sans Serif
Requirements
Must have
- Business cards and postcards must have a head shot on them.

```html
<!DOCTYPE html>
<html lang="en">
<head>
<meta charset="utf-8">
<title>Harbourline Group – Stationery Set</title>
<link href="https://fonts.googleapis.com/css2?family=Roboto:wght@400;500;700&display=swap" rel="stylesheet">
<style>
  :root {
    --brand-blue: #22399b;
    --brand-blue-dark: #1b2f85;
    --accent-red: #d6202f;
    --paper: #ffffff;
    --paper-grey: #f3f4f6;
    --stage: #e6e7e9;
    --rule: #b9bcc4;
    --photo-light: #cfc9c4;
    --photo-dark: #3b3a40;
  }
  * { box-sizing: border-box; margin: 0; padding: 0; }
  html, body { width: 1200px; height: 642px; overflow: hidden; }
  body {
    background: var(--stage);
    font-family: "Roboto", Arial, sans-serif;
  }
  .stage { position: relative; width: 1200px; height: 642px; overflow: hidden; }
  .piece { position: absolute; box-shadow: 0 2px 6px rgba(0,0,0,0.18); overflow: hidden; }

  .wordmark {
    font-family: "Roboto", Arial, sans-serif;
    font-weight: 700;
    line-height: 1;
    letter-spacing: -0.2px;
    text-align: center;
    white-space: nowrap;
  }
  .wordmark--light { color: var(--paper); }
  .wordmark--dark { color: var(--brand-blue); }

  /* Folder cover */
  .folder-cover {
    left: 70px; top: 90px; width: 210px; height: 385px;
    background: var(--brand-blue);
  }
  .folder-cover .wordmark { position: absolute; left: 0; right: 0; top: 168px; font-size: 22px; }
  .folder-cover__url {
    position: absolute; left: 0; right: 0; bottom: 30px;
    text-align: center; color: var(--paper); font-size: 11px;
  }

  /* Folder inside spread */
  .folder-spread { left: 388px; top: 108px; width: 380px; height: 356px; background: var(--paper); }
  .folder-spread__panel { position: absolute; top: 0; width: 190px; height: 356px; background: var(--paper-grey); }
  .folder-spread__panel--left { left: 0; background: var(--paper); }
  .folder-spread__panel--right { left: 190px; border-left: 1px solid #dcdde0; }
  .folder-spread__panel .wordmark { position: absolute; left: 0; right: 0; top: 146px; font-size: 19px; }
  .folder-pocket {
    position: absolute; left: 0; right: 0; bottom: 0; height: 110px;
    background: var(--brand-blue);
  }
  .folder-pocket svg { position: absolute; left: 0; top: 0; }
  .card-slot {
    position: absolute; left: 48px; top: 22px; width: 84px; height: 50px;
    background: var(--paper); box-shadow: 0 1px 3px rgba(0,0,0,0.25);
  }

  /* Postcard front */
  .postcard-front { left: 836px; top: 119px; width: 294px; height: 208px; background: var(--brand-blue); }
  .postcard-front svg { position: absolute; left: 0; top: 0; }
  .postcard-front .wordmark { position: absolute; left: 14px; width: 110px; top: 44px; font-size: 17px; }
  .postcard-front__contact {
    position: absolute; left: 13px; top: 134px;
    color: var(--paper); font-size: 9.5px; line-height: 14px;
  }
  .postcard-front__url {
    position: absolute; left: 13px; bottom: 16px;
    color: var(--paper); font-size: 9.5px;
  }

  /* Postcard back */
  .postcard-back { left: 832px; top: 353px; width: 296px; height: 209px; background: var(--paper); }
  .postcard-back__message {
    position: absolute; left: 0; top: 0; width: 146px; height: 100%;
    padding: 14px 10px 0 13px; color: var(--brand-blue);
    font-size: 6.2px; line-height: 9.2px;
  }
  .postcard-back__message p + p { margin-top: 9px; }
  .postcard-back__address-side {
    position: absolute; left: 146px; top: 0; right: 0; height: 100%;
    background: var(--paper-grey);
  }
  .stamp-box {
    position: absolute; right: 14px; top: 16px; width: 45px; height: 45px;
    border: 1px solid #9a9ca3; background: var(--paper);
  }
  .address-line { position: absolute; left: 13px; right: 14px; height: 1px; background: var(--rule); }

  /* Business cards */
  .card { top: 498px; width: 200px; height: 116px; background: var(--brand-blue); }
  .card--front { left: 316px; }
  .card--back { left: 532px; }
  .card svg { position: absolute; left: 0; top: 0; }
  .card--front .wordmark { position: absolute; left: 8px; width: 90px; top: 18px; font-size: 11.5px; }
  .card--back .wordmark { position: absolute; left: 0; right: 0; top: 52px; font-size: 17px; }
  .card__name {
    position: absolute; left: 9px; top: 52px;
    color: var(--paper); font-size: 7px; font-weight: 500; letter-spacing: 0.5px;
  }
  .card__role { position: absolute; left: 9px; top: 62px; color: var(--paper); font-size: 4.6px; }
  .card__address {
    position: absolute; left: 9px; top: 72px;
    color: var(--paper); font-size: 4.6px; line-height: 6.4px;
  }
  .card__contact {
    position: absolute; left: 9px; top: 88px; list-style: none;
    color: var(--paper); font-size: 4.6px; line-height: 6.6px;
  }
  .card__contact li { display: flex; align-items: center; gap: 3px; }
  .card__contact svg { position: static; }
</style>
</head>
<body>
<main class="stage">

  <!-- Pocket folder: outer cover -->
  <section class="piece folder-cover" aria-label="Pocket folder cover">
    <div class="wordmark wordmark--light">Harbourline Group</div>
    <div class="folder-cover__url">www.harbourlinegroup.com</div>
  </section>

  <!-- Pocket folder: inside spread -->
  <section class="piece folder-spread" aria-label="Pocket folder inside">
    <div class="folder-spread__panel folder-spread__panel--left">
      <div class="wordmark wordmark--dark">Harbourline Group</div>
      <div class="folder-pocket">
        <svg width="190" height="110" viewBox="0 0 190 110" aria-hidden="true">
          <path d="M40 34 C70 32 88 32 96 32 A8 8 0 0 0 112 32 C124 32 140 33 150 34" fill="none" stroke="#1a2c78" stroke-width="1"/>
        </svg>
      </div>
    </div>
    <div class="folder-spread__panel folder-spread__panel--right">
      <div class="wordmark wordmark--dark">Harbourline Group</div>
      <div class="folder-pocket">
        <div class="card-slot"></div>
      </div>
    </div>
  </section>

  <!-- Postcard front -->
  <section class="piece postcard-front" aria-label="Postcard front">
    <svg width="294" height="208" viewBox="0 0 294 208">
      <defs>
        <linearGradient id="postcardPhoto" x1="0" y1="0" x2="0" y2="1">
          <stop offset="0" stop-color="var(--photo-light)"/>
          <stop offset="1" stop-color="var(--photo-dark)"/>
        </linearGradient>
      </defs>
      <path d="M160 0 A100 140 0 0 0 160 208 L294 208 L294 0 Z" fill="#ffffff"/>
      <path d="M166 0 A96 140 0 0 0 166 208 L294 208 L294 0 Z" fill="url(#postcardPhoto)" role="img" aria-label="Head shot of the team director"/>
      <path d="M160 0 A100 140 0 0 0 160 208" fill="none" stroke="var(--accent-red)" stroke-width="2"/>
    </svg>
    <div class="wordmark wordmark--light">Harbourline Group</div>
    <div class="postcard-front__contact">
      <div>(555) 014-2290</div>
      <div>info@harbourlinegroup.com</div>
    </div>
    <div class="postcard-front__url">www.harbourlinegroup.com</div>
  </section>

  <!-- Postcard back -->
  <section class="piece postcard-back" aria-label="Postcard back">
    <div class="postcard-back__message">
      <p>42b Kerr Lane,<br>Lakeford, NZ, 8040</p>
      <p>(555) 014-2290<br>info@harbourlinegroup.com<br>www.harbourlinegroup.com</p>
      <p>There are many variations of passages of Lorem Ipsum available, but the majority have suffered alteration in some form, by injected humour, or randomised words which don't look even slightly believable. If you are going to use a passage of Lorem Ipsum, you need to be sure there isn't anything embarrassing hidden in the middle of text. All the Lorem Ipsum generators on the Internet tend to repeat predefined chunks as necessary, making this the Ipsum, you need to be sure there isn't</p>
    </div>
    <div class="postcard-back__address-side">
      <div class="stamp-box"></div>
      <div class="address-line" style="top:84px"></div>
      <div class="address-line" style="top:119px"></div>
      <div class="address-line" style="top:154px"></div>
      <div class="address-line" style="top:189px"></div>
    </div>
  </section>

  <!-- Business card front -->
  <section class="piece card card--front" aria-label="Business card front">
    <svg width="200" height="116" viewBox="0 0 200 116">
      <defs>
        <linearGradient id="cardPhoto" x1="0" y1="0" x2="0" y2="1">
          <stop offset="0" stop-color="var(--photo-light)"/>
          <stop offset="1" stop-color="var(--photo-dark)"/>
        </linearGradient>
      </defs>
      <path d="M124 0 A62 78 0 0 0 124 116 L200 116 L200 0 Z" fill="#ffffff"/>
      <path d="M128 0 A59 78 0 0 0 128 116 L200 116 L200 0 Z" fill="url(#cardPhoto)" role="img" aria-label="Head shot of the team member"/>
      <path d="M124 0 A62 78 0 0 0 124 116" fill="none" stroke="var(--accent-red)" stroke-width="1.5"/>
    </svg>
    <div class="wordmark wordmark--light">Harbourline Group</div>
    <div class="card__name">DANIEL REEVE</div>
    <div class="card__role">Director</div>
    <div class="card__address">42b Kerr Lane,<br>Lakeford, NZ, 8040</div>
    <ul class="card__contact">
      <li><svg width="5" height="5" viewBox="0 0 10 10" aria-hidden="true"><path d="M2 1 L4 1 L5 3.5 L3.8 4.5 A6 6 0 0 0 5.5 6.2 L6.5 5 L9 6 L9 8 A1 1 0 0 1 8 9 A7 7 0 0 1 1 2 A1 1 0 0 1 2 1 Z" fill="#fff"/></svg>(555) 014-2290</li>
      <li><svg width="5" height="5" viewBox="0 0 10 10" aria-hidden="true"><rect x="1" y="2" width="8" height="6" fill="none" stroke="#fff" stroke-width="1.2"/><path d="M1 2 L5 5.5 L9 2" fill="none" stroke="#fff" stroke-width="1.2"/></svg>info@harbourlinegroup.com</li>
      <li><svg width="5" height="5" viewBox="0 0 10 10" aria-hidden="true"><circle cx="5" cy="5" r="4" fill="none" stroke="#fff" stroke-width="1.2"/><path d="M1 5 H9 M5 1 C3 3.5 3 6.5 5 9 C7 6.5 7 3.5 5 1" fill="none" stroke="#fff" stroke-width="0.9"/></svg>www.harbourlinegroup.com</li>
    </ul>
  </section>

  <!-- Business card back -->
  <section class="piece card card--back" aria-label="Business card back">
    <div class="wordmark wordmark--light">Harbourline Group</div>
  </section>

</main>
</body>
</html>
```